Logo and website for new private wealth management business

This project is for a new company website and logo. The name of the firm is Harborline Estate Partners, LLC. We are a wealth management firm offering customized financial planning and investment management services to high net worth and ultra high net worth individuals and families. I want the website to feel contemporary but convey a feeling of sophistication and prestige.
www.tallowridgeholdings.example and www.qnfunds.example are both good reference websites.
My clients will consist of wealthy individuals and families. I have existing clients in their 50s - 70s, but I also intend to target younger business owners and entrepreneurs in their 30s -50s.

Target Market(s)

Business owners, entrepreneurs and corporate executives. Many existing clients are in their 60s and 70s, but intend to also attract a younger clientele in their 30s - 50s.

Industry/Entity Type

Wealth management, investment advisory, financial planning

Coding

Coded - Design and coding required

Colors
0054AA
0677BA
7BADD7
CADEEF
E8F1F8
0094D4
00A9DD
6FCCEA
C7EBF8
E9F6FB
00AB8E
00BBA5
67D7C9
C6EFE9
E9F9F6
EE7325
F08F49
F5BC92
FAE3D3
FDF4ED

Requirements
Must have
• Should use blue as the main color theme. Should have an About, Services, Our Clients, FAQ, and Contact sections
Should not have
• Should not have pictures of people as the background.

```html
<!DOCTYPE html>
<html lang="en">
<head>
<meta charset="utf-8">
<title>Harborline Estate Partners, LLC</title>
<link href="https://fonts.googleapis.com/css2?family=League+Spartan:wght@400;500;600;700&family=Poppins:wght@600;700&display=swap" rel="stylesheet">
<style>
:root{
  --navy:#0054AA;
  --blue:#0094D4;
  --blue-mid:#0677BA;
  --sky:#7BADD7;
  --orange:#F08F49;
  --ink:#1d1d1f;
  --text:#3b3b3b;
  --grey-bg:#f1f1f1;
  --line:#d9d9d9;
  --footer:#333333;
  --white:#ffffff;
}
*{box-sizing:border-box;margin:0;padding:0}
html,body{width:1200px;height:3788px;overflow:hidden}
body{font-family:"League Spartan",Arial,sans-serif;color:var(--text);background:var(--white);position:relative}
.abs{position:absolute}
.btn{position:absolute;background:var(--orange);color:var(--white);font-size:14px;font-weight:500;letter-spacing:.5px;display:flex;align-items:center;justify-content:center;border-radius:3px;text-transform:uppercase}
.section-title{position:absolute;left:0;width:1200px;text-align:center;font-size:35px;font-weight:600;color:var(--navy);letter-spacing:.5px}
.section-title span{color:var(--blue)}

/* header */
.site-header{top:0;left:0;width:1200px;height:103px;background:var(--white);border-bottom:1px solid #eee}
.brand-mark{left:162px;top:16px;width:70px;height:70px;border-radius:50%;border:4px solid var(--navy)}
.brand-name{left:246px;top:24px;width:170px;font-size:17px;font-weight:600;line-height:19px;color:var(--ink);text-transform:uppercase}
.main-nav{left:441px;top:44px;display:flex;gap:34px;font-size:14px;font-weight:600;color:var(--ink)}
.main-nav .active{color:var(--blue)}
.nav-contact{left:912px;top:29px;width:126px;height:45px}

/* hero */
.hero{top:103px;left:0;width:1200px;height:517px;background:linear-gradient(180deg,#e59a66 0%,#f1a86b 25%,#9a6a5a 55%,#4b4a55 75%,#3c3f48 100%)}
.hero h1{position:absolute;left:150px;width:900px;top:337px;text-align:center;font-family:"Poppins",Arial,sans-serif;font-size:31px;line-height:45px;font-weight:700;color:var(--white);text-shadow:0 2px 6px rgba(0,0,0,.45)}

/* about */
.about-photo{left:154px;top:710px;width:406px;height:406px;border-radius:50%;border:2px solid var(--blue);padding:7px}
.about-photo div{width:100%;height:100%;border-radius:50%;background:radial-gradient(circle at 50% 40%,#d9a39a 0%,#8b8f9c 55%,#3f5872 100%)}
.about-kicker{left:619px;top:713px;font-size:15px;font-weight:600;color:var(--navy)}
.about-title{left:619px;top:734px;font-size:36px;line-height:45px;font-weight:600;color:var(--blue);letter-spacing:1px}
.about-copy{left:619px;top:828px;width:420px;font-size:13.4px;line-height:24.3px;color:var(--text)}
.about-copy p+p{margin-top:9px}
.about-btn{left:619px;top:1070px;width:134px;height:43px}

/* services */
.services{top:1196px;left:0;width:1200px;height:613px;background:var(--grey-bg)}
.card{position:absolute;top:148px;width:202px;height:299px;background:var(--white);box-shadow:0 4px 10px rgba(0,0,0,.08);text-align:center}
.card-photo{width:100%;height:158px}
.card-icon{position:absolute;left:71px;top:128px;width:60px;height:60px;border-radius:50%;background:var(--white);display:flex;align-items:center;justify-content:center}
.card h3{margin-top:40px;font-size:15px;line-height:19px;font-weight:600;color:var(--ink)}
.card p{margin-top:10px;font-size:11.5px;line-height:22px;color:var(--text);padding:0 18px}
.services-btn{left:532px;top:479px;width:134px;height:43px}

/* clients */
.client{position:absolute;top:1960px;width:160px;height:105px;border:1px solid #e3e3e3;background:var(--white);display:flex;align-items:center;justify-content:center;gap:8px;font-size:25px;font-weight:500;color:#9a9a9a}
.client.active{border:2px solid var(--blue);color:var(--ink)}
.client i{width:14px;height:14px;border-radius:50%;background:currentColor;display:block}
.dots{left:571px;top:2099px;display:flex;gap:8px}
.dots b{width:9px;height:9px;border-radius:50%;background:#b9b9b9;display:block}
.dots b.on{background:var(--navy)}

/* faq */
.faq{top:2199px;left:0;width:1200px;height:683px;background:var(--grey-bg)}
.faq-rail{left:242px;top:2360px;width:2px;height:400px;background:var(--blue)}
.faq-item{position:absolute;left:213px;width:772px;height:47px;background:var(--white);border:1px solid var(--line);display:flex;align-items:center;font-size:13.5px;font-weight:600;color:var(--ink)}
.faq-item .node{position:absolute;left:21px;top:16px;width:15px;height:15px;border-radius:50%;border:2px solid var(--blue);background:var(--white)}
.faq-item .label{margin-left:51px}
.faq-item .toggle{position:absolute;right:-1px;top:-1px;width:47px;height:47px;background:var(--navy);display:flex;align-items:center;justify-content:center}
.faq-item.open{background:var(--blue);border-color:var(--blue);color:var(--white)}
.faq-item.open .node{border-color:var(--white);background:var(--blue)}
.faq-item.open .toggle{background:var(--blue)}
.faq-answer{left:258px;top:2544px;width:690px;font-size:13px;line-height:24.5px;color:var(--text)}

/* contact */
.field{position:absolute;height:43px;border:1px solid var(--line);background:var(--white);display:flex;align-items:center;font-size:11.5px;color:#444}
.field .ic{width:36px;height:100%;border-right:1px solid var(--line);display:flex;align-items:center;justify-content:center;margin-right:15px}
.field.msg{align-items:flex-start;height:88px}
.field.msg .ic{height:43px;border-right:none}
.field.msg span{margin-top:16px}
.submit-btn{left:532px;top:3265px;width:134px;height:43px}

/* footer */
.site-footer{top:3398px;left:0;width:1200px;height:349px;background:var(--footer);color:#e9e9e9}
.foot-head{position:absolute;top:66px;font-size:14px;font-weight:600;letter-spacing:.5px;color:var(--white)}
.foot-head::after{content:"";display:block;width:30px;height:2px;background:#cfcfcf;margin-top:9px}
.quick-links{position:absolute;left:162px;top:118px;font-size:12px;line-height:29.5px;list-style:none}
.detail{position:absolute;left:353px;display:flex;gap:11px;font-size:12px;line-height:20px}
.detail strong{font-weight:600;font-size:13px;display:block;color:var(--white)}
.social{position:absolute;left:685px;display:flex;align-items:center;gap:9px;font-size:12.5px}
.social i{width:29px;height:29px;border-radius:50%;border:1.5px solid #e9e9e9;display:block}
.foot-mark{left:874px;top:3489px;width:165px;height:165px;border-radius:50%;border:5px solid #9c9c9c;display:flex;align-items:center;justify-content:center;font-size:20px;font-weight:600;color:#9c9c9c}
.copyright{top:3747px;left:0;width:1200px;height:41px;background:var(--navy);color:var(--white);font-size:11.5px;display:flex;align-items:center;justify-content:center}
</style>
</head>
<body>

<header class="site-header abs">
  <div class="brand-mark abs"></div>
  <div class="brand-name abs">Harborline Estate Partners, LLC</div>
  <nav class="main-nav abs">
    <span class="active">HOME</span><span>ABOUT</span><span>SERVICES</span><span>OUR CLIENTS</span><span>FAQs</span>
  </nav>
  <a class="btn nav-contact">Contact</a>
</header>

<section class="hero abs" role="img" aria-label="City skyline and suspension bridge at sunset over the river">
  <h1>We Are A Wealth Management Firm Offering Customized Financial Planning And Investment Management Services</h1>
</section>

<section class="about">
  <div class="about-photo abs"><div role="img" aria-label="Chess king piece in front of rising financial charts"></div></div>
  <div class="about-kicker abs">ABOUT</div>
  <h2 class="about-title abs">HARBORLINE ESTATE<br>PARTNERS, LLC.</h2>
  <div class="about-copy abs">
    <p>Lorem ipsum dolor sit amet consectetuer adipiscig elit nonummy nibh euismod tincidunt ut laoreet dolore ma aliquam erat volutpat. Ut wisi enim ad minim veniam quis.</p>
    <p>Lorem ipsum dolor sit amet, consectetuer adipisci sed d nonummy nibh euismod tincidunt ut laoreet dolore magna alim erat volutpat. Ut wisi enim ad minim veniam, quis nostrud exercion ullrper suscipit lobortis nisl ut aliquip ex ea commodo consequat. Duis autem vel eum iriure dolor in hendrerit in vulputate velit esse stie consequat, vel illum dolore eu feugiat nulla facilisis at vero eros.</p>
  </div>
  <a class="btn about-btn">Contact Us</a>
</section>

<section class="services abs">
  <h2 class="section-title" style="top:83px">OUR <span>SERVICES</span></h2>
  <div class="card" style="left:162px">
    <div class="card-photo" role="img" aria-label="Advisor reviewing printed charts" style="background:linear-gradient(135deg,#6f6a66,#c9c3bb)"></div>
    <div class="card-icon"><svg width="34" height="34" viewBox="0 0 34 34" fill="none" stroke="#0054AA" stroke-width="1.6"><rect x="6" y="20" width="4" height="10"/><rect x="14" y="14" width="4" height="16"/><rect x="22" y="8" width="4" height="22"/><path d="M4 16 L14 8 L20 12 L30 4"/></svg></div>
    <h3>Financial<br>Planning</h3><p>Lorem ipsum dolor sit amet consectetuer adipiing elit.</p>
  </div>
  <div class="card" style="left:386px">
    <div class="card-photo" role="img" aria-label="Desk with laptop and financial reports" style="background:linear-gradient(135deg,#8d8b8a,#d8d3cc)"></div>
    <div class="card-icon"><svg width="34" height="34" viewBox="0 0 34 34" fill="none" stroke="#0054AA" stroke-width="1.6"><rect x="5" y="7" width="22" height="16" rx="1"/><path d="M9 12h14M9 16h10"/><circle cx="25" cy="25" r="5"/></svg></div>
    <h3>Financial<br>Planning</h3><p>Lorem ipsum dolor sit amet consectetuer adipiing elit.</p>
  </div>
  <div class="card" style="left:611px">
    <div class="card-photo" role="img" aria-label="Tablet held before a city skyline" style="background:linear-gradient(135deg,#2f3c55,#9eb0c8)"></div>
    <div class="card-icon"><svg width="34" height="34" viewBox="0 0 34 34" fill="none" stroke="#0054AA" stroke-width="1.6"><circle cx="21" cy="12" r="8"/><path d="M21 8v8M5 30V20M10 30V16M15 30V22M3 30h28"/></svg></div>
    <h3>Financial<br>Planning</h3><p>Lorem ipsum dolor sit amet consectetuer adipiing elit.</p>
  </div>
  <div class="card" style="left:836px">
    <div class="card-photo" role="img" aria-label="Meeting table with printed charts" style="background:linear-gradient(135deg,#b9c2cc,#eef0f3)"></div>
    <div class="card-icon"><svg width="34" height="34" viewBox="0 0 34 34" fill="none" stroke="#0054AA" stroke-width="1.6"><circle cx="20" cy="10" r="6"/><path d="M4 24l8-4h8l-2 3h-6M4 30l6-3h10l9-7"/></svg></div>
    <h3>Financial<br>Planning</h3><p>Lorem ipsum dolor sit amet consectetuer adipiing elit.</p>
  </div>
  <a class="btn services-btn">Contact Us</a>
</section>

<h2 class="section-title" style="top:1890px">OUR <span>CLIENTS</span></h2>
<div class="client" style="left:162px"><i></i>Corvane</div>
<div class="client active" style="left:341px"><i></i>Tidemark</div>
<div class="client" style="left:520px"><i></i>Lumora</div>
<div class="client" style="left:700px"><i></i>Brisell</div>
<div class="client" style="left:879px"><i></i>Oakvey</div>
<div class="dots abs"><b></b><b class="on"></b><b></b><b></b></div>

<section class="faq abs"></section>
<h2 class="section-title" style="top:2280px">FREQURNTLY ASKED <span>QUESTIONS</span></h2>
<div class="faq-rail abs"></div>
<div class="faq-item" style="top:2345px"><span class="node"></span><span class="label">Lorem Ipsum Is Simply Dummy Text Of The Printing Sheets Containing</span><span class="toggle"><svg width="22" height="22" viewBox="0 0 22 22" fill="none" stroke="#fff" stroke-width="1.5"><circle cx="11" cy="11" r="9.5"/><path d="M11 6v10M6 11h10"/></svg></span></div>
<div class="faq-item" style="top:2412px"><span class="node"></span><span class="label">Consectetuer Adipiscing Elit Sed Diam Nonummy Nibh</span><span class="toggle"><svg width="22" height="22" viewBox="0 0 22 22" fill="none" stroke="#fff" stroke-width="1.5"><circle cx="11" cy="11" r="9.5"/><path d="M11 6v10M6 11h10"/></svg></span></div>
<div class="faq-item open" style="top:2478px"><span class="node"></span><span class="label">Printer took a galley of type and scrambled</span><span class="toggle"><svg width="22" height="22" viewBox="0 0 22 22" fill="none" stroke="#fff" stroke-width="1.5"><circle cx="11" cy="11" r="9.5"/><path d="M6 11h10"/></svg></span></div>
<div class="faq-answer abs">Lorem ipsum dolor sit amet, consectetuer adipiscing elit, sed diam nonummy nibh euismod tincidunt laoreet dolore magna aliquam erat volutpat. Ut wisi enim ad minim veniam, quis nostrud exerci tation ullarper suscipit lobortis nisl ut aliquip ex ea commodo consequat. Duis autem vel eum iriure dolor in hendrerit in vulputate velit esse molestie consequat, vel illum dolore eu feugiat nulla facilisis at vero eros et accun et iusto odio dignissim qui blandit praesent luptatum zzril delenit augue duis dolore te feugait nulla facilisi.</div>
<div class="faq-item" style="top:2679px"><span class="node"></span><span class="label">Duis Autem Vel Eum Iriure Dolor In Hendrerit In Vulputate Velit</span><span class="toggle"><svg width="22" height="22" viewBox="0 0 22 22" fill="none" stroke="#fff" stroke-width="1.5"><circle cx="11" cy="11" r="9.5"/><path d="M11 6v10M6 11h10"/></svg></span></div>
<div class="faq-item" style="top:2744px"><span class="node"></span><span class="label">Ut Wisi Enim Ad Minim Veniam, Quis Nostrud Exerci Tation</span><span class="toggle"><svg width="22" height="22" viewBox="0 0 22 22" fill="none" stroke="#fff" stroke-width="1.5"><circle cx="11" cy="11" r="9.5"/><path d="M11 6v10M6 11h10"/></svg></span></div>

<h2 class="section-title" style="top:2962px">QUICK <span>CONTACT</span></h2>
<div class="field" style="left:284px;top:3031px;width:307px"><span class="ic"><svg width="12" height="12" viewBox="0 0 12 12" fill="#0094D4"><circle cx="6" cy="3.5" r="3"/><path d="M0 12c0-4 3-5.5 6-5.5s6 1.5 6 5.5z"/></svg></span>First Name*</div>
<div class="field" style="left:607px;top:3031px;width:308px"><span class="ic"><svg width="12" height="12" viewBox="0 0 12 12" fill="#0094D4"><circle cx="6" cy="3.5" r="3"/><path d="M0 12c0-4 3-5.5 6-5.5s6 1.5 6 5.5z"/></svg></span>Last Name*</div>
<div class="field" style="left:284px;top:3090px;width:307px"><span class="ic"><svg width="12" height="12" viewBox="0 0 12 12" fill="#0094D4"><path d="M2 0l2.5 3-1.2 1.5c.8 1.8 2.2 3.2 4 4L8.8 7.3 12 9.8 10.5 12C5 11.5.5 7 0 1.5z"/></svg></span>Your Phone*</div>
<div class="field" style="left:607px;top:3090px;width:308px"><span class="ic"><svg width="13" height="10" viewBox="0 0 13 10" fill="#0094D4"><path d="M0 0h13v1.5L6.5 5.5 0 1.5zM0 3l6.5 4L13 3v7H0z"/></svg></span>Your Email*</div>
<div class="field msg" style="left:284px;top:3149px;width:631px"><span class="ic"><svg width="13" height="11" viewBox="0 0 13 11" fill="#0094D4"><ellipse cx="5.5" cy="4" rx="5.5" ry="4"/><ellipse cx="9" cy="7" rx="4" ry="3"/></svg></span><span>Your Message</span></div>
<a class="btn submit-btn">Submit Now</a>

<footer class="site-footer abs">
  <div class="foot-head" style="left:162px">QUICK LINKS</div>
  <ul class="quick-links">
    <li>• Home</li><li>• About Us</li><li>• Services</li><li>• Our Clients</li><li>• FAQs</li><li>• Contact</li>
  </ul>
  <div class="foot-head" style="left:353px">CONTACT DETAILS</div>
  <div class="detail" style="top:118px"><svg width="12" height="16" viewBox="0 0 12 16" fill="#fff"><path d="M6 0a6 6 0 0 1 6 6c0 4-6 10-6 10S0 10 0 6a6 6 0 0 1 6-6zm0 3.5a2.5 2.5 0 1 0 0 5 2.5 2.5 0 0 0 0-5z"/></svg><div><strong>ADDRESS</strong>123 Ut Wisi Enim Ad Minim<br>Veniam Quis Nostrud.</div></div>
  <div class="detail" style="top:199px"><svg width="13" height="13" viewBox="0 0 12 12" fill="#fff"><path d="M2 0l2.5 3-1.2 1.5c.8 1.8 2.2 3.2 4 4L8.8 7.3 12 9.8 10.5 12C5 11.5.5 7 0 1.5z"/></svg><div><strong>PHONE</strong>123 456 7890</div></div>
  <div class="detail" style="top:259px"><svg width="14" height="11" viewBox="0 0 13 10" fill="#fff"><path d="M0 0h13v1.5L6.5 5.5 0 1.5zM0 3l6.5 4L13 3v7H0z"/></svg><div><strong>EMAIL</strong>info@harborlineestate.example</div></div>
  <div class="foot-head" style="left:685px">FOLLOW US</div>
  <div class="social" style="top:117px"><i></i>Community</div>
  <div class="social" style="top:160px"><i></i>Video Channel</div>
  <div class="social" style="top:204px"><i></i>Photo Feed</div>
  <div class="social" style="top:248px"><i></i>News Feed</div>
</footer>
<div class="foot-mark abs">Harborline</div>
<div class="copyright abs">© 2023 HARBORLINE ESTATE PARTNERS, LLC. All Rights Reserved.</div>

</body>
</html>
```